Business Card for Fashion House

We need a business card design for our personalize fashion service for our customers. the business card should reflect reliability, luxury and creativity.
The brand Gravetto is extracted from "Graceful Vetto"; Gravetto provides fashion designs sprinkled with luxury and style tailored for our elite clients character profile.
Gravetto is created for those who embody class and elegance with a passion for style.
Target Market(s)
Affluent Customers
Industry/Entity Type
Fashion
Contact Information for Business Card
Rania Bou Khalil
Fashion Designer
Telephone: +971 5550123
Mobile +971 555987
Emal q@z.com
Website www.gravetto-example.com
Social Media Youtube g+ Facebook Instagram Pin /gravetto
Font styles to use
Other font styles liked:
- Audrey provided
Look and feel
Each slider illustrates characteristics of the customer's brand and the style your logo design should communicate.

```html
<!DOCTYPE html>
<html lang="en">
<head>
<meta charset="utf-8">
<title>Gravetto Business Card</title>
<link href="https://fonts.googleapis.com/css2?family=Marcellus&family=Tenor+Sans&display=swap" rel="stylesheet">
<style>
  :root {
    --backdrop: #2b2f33;
    --card: #1f1c1c;
    --ink: #f2f2f2;
    --ink-soft: #c9c9c9;
  }
  * { margin: 0; padding: 0; box-sizing: border-box; }
  html, body { width: 1200px; height: 900px; overflow: hidden; }
  body {
    background: var(--backdrop);
    display: flex;
    flex-direction: column;
    align-items: center;
    justify-content: center;
    gap: 56px;
    font-family: "Tenor Sans", sans-serif;
    color: var(--ink);
  }
  .card {
    width: 620px;
    height: 354px;
    background: var(--card);
    border-radius: 26px;
    position: relative;
    box-shadow: 0 10px 28px rgba(0,0,0,.45);
  }
  /* Front */
  .card-front {
    display: flex;
    flex-direction: column;
    align-items: center;
    justify-content: center;
    gap: 30px;
  }
  .brand-name {
    font-family: "Marcellus", serif;
    font-size: 34px;
    letter-spacing: 14px;
    padding-left: 14px;
    color: var(--ink);
    font-weight: 400;
  }
  .social-handle {
    display: flex;
    align-items: center;
    gap: 10px;
    font-size: 15px;
    letter-spacing: 1px;
    color: var(--ink-soft);
  }
  .social-handle .dot {
    width: 8px; height: 8px; border-radius: 50%; background: var(--ink-soft);
  }
  /* Back */
  .card-back { display: flex; align-items: center; }
  .contact {
    width: 50%;
    padding: 0 0 0 44px;
    align-self: flex-start;
    margin-top: 44px;
  }
  .contact-name {
    font-family: "Marcellus", serif;
    font-size: 24px;
    font-weight: 400;
    color: var(--ink-soft);
  }
  .contact-role {
    font-size: 12px;
    color: #8f8f8f;
    margin-top: 2px;
    margin-bottom: 22px;
  }
  .contact-list { list-style: none; font-size: 14px; line-height: 1.55; color: var(--ink-soft); }
  .contact-list .label { display: inline-block; width: 30px; }
  .divider {
    position: absolute;
    left: 300px; top: 60px;
    width: 0; height: 234px;
    border-left: 2px solid var(--ink);
  }
  .back-brand {
    width: 50%;
    display: flex;
    justify-content: center;
    padding-left: 20px;
  }
  .back-brand .brand-name { font-size: 24px; letter-spacing: 10px; padding-left: 10px; }
</style>
</head>
<body>
  <section class="card card-front">
    <h1 class="brand-name">GRAVETTO</h1>
    <p class="social-handle"><span class="dot"></span>/gravetto</p>
  </section>

  <section class="card card-back">
    <div class="contact">
      <h2 class="contact-name">Rania Bou Khalil</h2>
      <p class="contact-role">Fashion Designer</p>
      <ul class="contact-list">
        <li><span class="label">T :</span>+971 5550123</li>
        <li><span class="label">M :</span>+971 555987</li>
        <li><span class="label">E :</span>q@z.com</li>
        <li><span class="label">W :</span>www.gravetto-example.com</li>
      </ul>
    </div>
    <span class="divider"></span>
    <div class="back-brand">
      <p class="brand-name">GRAVETTO</p>
    </div>
  </section>
</body>
</html>
```